Wealth Management Business Card

We are a professional services consulting firm that specializes in high net worth individuals over $25,000,000, executives C-suite and above, closely held businesses owners, family offices and highly compensated employees.

Our focus is on risk mitigation and tax efficient strategies. Our clients take their risk on themselves and have a proven track record generating wealth. Our directive is to preserve and protect the wealth they’ve already created.

Our company Harrowgate Advisory is geared around five directives of asset protection:
1) Legal Structuring
2) Leverage & Financing
3) Risk Management - Asset Protection & Insurance, Trustee Work
4) Asset Management & Investing - Under www.qlvbrookfield.com
5) Tax Efficient Strategies

Our Company Mark is a Pentagon with a key in the middle. A pentagon is the most efficient defensive structure. Each point of a pentagon is equal distance front every point . Each side provides support to another and works together, which is the key to our clients success.

Our key colors are blue, black and silver.

We ‘re located in the Pacific Northwest with bi coastal and international clients. We have fewer, higher net worth clients and provide exceptional customer service. We do not do social media.

website is www.harrowgatepath.com

Target Market(s)

High End Clients

Contact Information for Business Card

extra thick

Font styles to use
Serif

Requirements
Must have
• Metalic foil for lettering.
Black Background on one side
White Background on the other
Horizontal Format Only
No Rounded corners
Not Marketing sales information on the card.
Nice to have
• imprinted texture on the card
Should not have
• lots of color

```html
<!DOCTYPE html>
<html lang="en">
<head>
<meta charset="utf-8">
<title>Harrowgate Advisory – Business Card</title>
<link rel="stylesheet" href="https://fonts.googleapis.com/css2?family=Cinzel:wght@400;600&family=Old+Standard+TT:ital,wght@0,400;1,400&display=swap">
<style>
  :root {
    --backdrop: #262626;
    --front-top: #141416;
    --front-bottom: #0a0a0b;
    --back-paper: #ffffff;
    --silver: #c8ccd4;
    --silver-soft: #b4b8c1;
    --ink-navy: #141c4a;
    --ink-body: #2a2f45;
    --accent-sky: #1a8fd0;
    --accent-deep: #0f2f78;
    --tab-text: #ffffff;
  }
  * { margin: 0; padding: 0; box-sizing: border-box; }
  html, body {
    width: 1200px; height: 1138px; overflow: hidden;
    background: var(--backdrop);
  }
  .canvas { position: relative; width: 1200px; height: 1138px; }
  .card {
    position: absolute; left: 274px; width: 624px; height: 376px;
    overflow: hidden;
  }
  .card--front {
    top: 186px;
    background: linear-gradient(180deg, var(--front-top), var(--front-bottom));
  }
  .card--back { top: 606px; background: var(--back-paper); }

  .front-name {
    position: absolute; left: 0; right: 0; top: 156px;
    text-align: center;
    font-family: "Cinzel", serif; font-weight: 400;
    font-size: 34px; letter-spacing: 4px;
    color: var(--silver);
  }
  .services {
    position: absolute; left: 0; right: 0; top: 318px;
    text-align: center;
    font-family: "Old Standard TT", serif; font-size: 13.5px;
    line-height: 16px; color: var(--silver-soft);
  }
  .services .sep { color: var(--accent-sky); margin: 0 8px; }

  .person { position: absolute; left: 34px; top: 42px; }
  .person__name {
    font-family: "Cinzel", serif; font-weight: 600;
    font-size: 24px; color: var(--ink-navy); letter-spacing: 0.3px;
    line-height: 26px;
  }
  .person__title {
    font-family: "Old Standard TT", serif; font-style: italic;
    font-size: 16px; color: var(--ink-body); line-height: 18px;
  }

  .contact { position: absolute; left: 34px; top: 209px; list-style: none; }
  .contact__item {
    display: flex; align-items: center; height: 25px;
    font-family: "Old Standard TT", serif; font-size: 16px; color: var(--ink-body);
  }
  .contact__item svg { width: 22px; height: 22px; margin-right: 13px; }
  .address {
    position: absolute; left: 34px; top: 290px;
    font-family: "Old Standard TT", serif; font-size: 16px;
    line-height: 22px; color: var(--ink-body);
  }

  .brand-name {
    position: absolute; left: 304px; width: 280px; top: 212px;
    text-align: center;
    font-family: "Cinzel", serif; font-weight: 600;
    font-size: 27px; line-height: 33px; letter-spacing: 3px;
    color: var(--ink-navy);
  }

  .strip-sky {
    position: absolute; left: 0; bottom: 0; width: 258px; height: 15px;
    background: var(--accent-sky);
  }
  .tab { position: absolute; left: 0; bottom: 0; width: 624px; height: 47px; }
  .tab__label {
    position: absolute; left: 280px; right: 0; bottom: 12px;
    text-align: center;
    font-family: "Cinzel", serif; font-size: 17px; letter-spacing: 0.5px;
    color: var(--tab-text);
  }
</style>
</head>
<body>
<main class="canvas">
  <section class="card card--front" aria-label="Card front">
    <p class="front-name">HARROWGATE ADVISORY</p>
    <p class="services">
      LEGAL STRUCTURING<span class="sep">|</span>LEVERAGE &amp; FINANCING<span class="sep">|</span>RISK MANAGEMENT<br>
      ASSET MANAGEMENT &amp; INVESTING<span class="sep">|</span>TAX EFFICIENT STRATEGIES
    </p>
  </section>

  <section class="card card--back" aria-label="Card back">
    <div class="person">
      <p class="person__name">CORWIN ALDRIDGE</p>
      <p class="person__title">Financial Strategist</p>
    </div>

    <ul class="contact">
      <li class="contact__item">
        <svg viewBox="0 0 22 22" aria-hidden="true"><circle cx="11" cy="11" r="11" fill="var(--accent-sky)"/><path d="M7 6.5h2l1 2.5-1.3 1a6 6 0 0 0 2.8 2.8l1-1.3 2.5 1v2a1 1 0 0 1-1 1A8.5 8.5 0 0 1 6 7.5a1 1 0 0 1 1-1z" fill="#fff"/></svg>
        (503) 555-0148
      </li>
      <li class="contact__item">
        <svg viewBox="0 0 22 22" aria-hidden="true"><circle cx="11" cy="11" r="11" fill="var(--accent-sky)"/><rect x="5.5" y="7" width="11" height="8" fill="none" stroke="#fff" stroke-width="1.3"/><path d="M5.5 7l5.5 4.5L16.5 7" fill="none" stroke="#fff" stroke-width="1.3"/></svg>
        info@harrowgatepath.com
      </li>
      <li class="contact__item">
        <svg viewBox="0 0 22 22" aria-hidden="true"><circle cx="11" cy="11" r="11" fill="var(--accent-sky)"/><g fill="none" stroke="#fff" stroke-width="1.1"><circle cx="11" cy="11" r="5.5"/><ellipse cx="11" cy="11" rx="2.4" ry="5.5"/><path d="M5.5 11h11"/></g></svg>
        www.harrowgatepath.com
      </li>
    </ul>

    <p class="address">418 W Alder Ave, Suite 112,<br>Lake Grove, OR 97099</p>

    <p class="brand-name">HARROWGATE<br>ADVISORY</p>

    <div class="strip-sky"></div>
    <svg class="tab" viewBox="0 0 624 47" aria-hidden="true"><polygon points="276,0 624,0 624,47 250,47" fill="var(--accent-deep)"/></svg>
    <p class="tab__label">HARROWGATE ADVISORY LLC</p>
  </section>
</main>
</body>
</html>
```